Design an Exhibition Poster for our Web Application

Our company develops and sells VaultLarkly, a web-based service that helps small businesses to test their web applications for security vulnerabilities.

You can see details of the service at the following page:

https://www.vaultlarkly.example/

We need a poster designed, to be used on an exhibition stand at a professional security conference.

Reason: The deadline for this project is being extended because we have, so far, received very few design submissions and they are generally not of the aesthetic quality we are looking for.

Target Market(s)

Tech startups and small / medium sized online businesses

Industry/Entity Type

Security

Requirements
Must have
• [1] Incorporate the VaultLarkly logo (see attached file).

[2] Use the text supplied by us (see attached file).

[3] Use a color scheme that matches the scheme used on our website.

[4] Project the visual theme of cyber security (or protection against cyber crime).
Nice to have
• This is part of a 2-poster set. The project for designing the other poster in the set is also being listed on ArtHivePlace today. Please look for the project entitled "Design an Exhibition Poster for our Software Product".

Preference will be given to designers who submit a pair of designs that harmonize with each other.

```html
<!DOCTYPE html>
<html lang="en">
<head>
<meta charset="utf-8">
<title>VaultLarkly – Exhibition Poster Concepts</title>
<link href="https://fonts.googleapis.com/css2?family=Arimo:wght@400;700&display=swap" rel="stylesheet">
<style>
  :root {
    --canvas: #ffffff;
    --brand-green: #a3c45f;
    --brand-green-dark: #7f9f3f;
    --brand-grey: #808285;
    --ink: #1e1e1e;
    --body-grey: #7a7a7a;
    --tab-dark: #45484b;
    --tab-dark-edge: #6b6e71;
    --footer-top: #3a3a3a;
    --footer-bottom: #0f0f0f;
    --marker: #e6197e;
    --frame: #c9c9c9;
    --art-light: #e4e4e4;
    --art-mid: #8a8c8f;
    --art-dark: #505356;
  }
  * { margin: 0; padding: 0; box-sizing: border-box; }
  html, body { width: 1200px; height: 802px; overflow: hidden; background: var(--canvas); }
  body { position: relative; font-family: "Arimo", Arial, sans-serif; }

  .concept-number {
    position: absolute; width: 20px; height: 20px; border-radius: 50%;
    background: var(--marker); color: #fff; font-size: 13px;
    line-height: 20px; text-align: center;
  }

  .poster {
    position: absolute; top: 21px; width: 549px; height: 756px;
    border: 1px solid var(--frame); overflow: hidden;
    background: linear-gradient(180deg, #ffffff 0%, #f6f6f6 45%, #ececec 75%, #e2e2e2 100%);
  }
  .poster--centered { left: 45px; }
  .poster--right { left: 629px; }

  .poster__art {
    position: absolute; left: 0; right: 0; top: 500px; height: 198px;
    background: linear-gradient(180deg, rgba(228,228,228,0) 0%, var(--art-light) 30%, var(--art-mid) 62%, var(--art-dark) 100%);
  }

  .brand { position: absolute; display: flex; align-items: center; }
  .brand__mark { background: var(--brand-green); flex: none; }
  .brand__name { color: var(--brand-grey); font-weight: 700; letter-spacing: 0.5px; line-height: 1; }

  .poster--centered .brand { left: 0; right: 0; top: 82px; height: 66px; justify-content: center; gap: 22px; }
  .poster--centered .brand__mark { width: 64px; height: 64px; }
  .poster--centered .brand__name { font-size: 60px; }

  .poster--right .brand { left: 40px; top: 52px; height: 72px; gap: 24px; }
  .poster--right .brand__mark { width: 72px; height: 72px; }
  .poster--right .brand__name { font-size: 66px; }

  .headline {
    position: absolute; left: 0; right: 0; color: var(--brand-green);
    font-weight: 700; font-size: 30px; line-height: 34px; letter-spacing: 0.2px;
  }
  .intro {
    position: absolute; left: 0; right: 0; color: var(--ink);
    font-size: 15.5px; line-height: 19px;
  }
  .feature { position: absolute; left: 0; right: 0; }
  .feature__tab {
    position: absolute; height: 24px; color: #fff; font-weight: 700;
    font-size: 19px; line-height: 24px;
  }
  .feature__text {
    position: absolute; left: 0; right: 0; color: var(--body-grey);
    font-size: 14.5px; line-height: 18px;
  }

  /* centred variant */
  .poster--centered .headline { top: 233px; text-align: center; }
  .poster--centered .intro { top: 251px; text-align: center; margin-top: 10px; }
  .poster--centered .feature__tab {
    left: 205px; width: 138px; text-align: center;
    background: linear-gradient(90deg, var(--tab-dark) 0%, #55585b 100%);
    clip-path: polygon(10px 0, 100% 0, calc(100% - 10px) 100%, 0 100%);
    box-shadow: inset -3px 0 0 var(--tab-dark-edge);
  }
  .poster--centered .feature__text { top: 28px; text-align: center; }
  .poster--centered .feature--simple .feature__text { line-height: 22px; top: 25px; }

  /* right-aligned variant */
  .poster--right .headline { top: 201px; right: 37px; text-align: right; font-size: 27px; }
  .poster--right .intro { top: 236px; right: 37px; text-align: right; font-size: 14px; line-height: 17px; }
  .poster--right .feature__tab {
    right: 27px; left: auto; width: 141px; height: 26px; line-height: 26px; padding-right: 12px; text-align: right;
    background: linear-gradient(90deg, #8fb24b 0%, var(--brand-green) 100%);
    clip-path: polygon(8px 0, 100% 0, 100% 100%, 0 100%);
    box-shadow: inset -5px 0 0 var(--brand-green-dark);
  }
  .poster--right .feature__text { top: 31px; right: 37px; text-align: right; }

  .footer {
    position: absolute; left: 0; right: 0; bottom: 0; height: 59px;
    border-top: 4px solid var(--brand-green);
    background: linear-gradient(180deg, var(--footer-top) 0%, var(--footer-bottom) 100%);
    text-align: center; color: #fff;
  }
  .footer__url { margin-top: 5px; font-size: 19px; line-height: 22px; font-weight: 700; }
  .footer__cta { margin-top: 2px; font-size: 14px; line-height: 18px; }
</style>
</head>
<body>

  <span class="concept-number" style="left:8px; top:13px;">3</span>
  <span class="concept-number" style="left:605px; top:13px;">4</span>

  <section class="poster poster--centered">
    <div class="poster__art" role="img" aria-label="Abstract angular backdrop in grey and green tones"></div>

    <div class="brand">
      <span class="brand__mark"></span>
      <span class="brand__name">VaultLarkly</span>
    </div>

    <h1 class="headline">SECURITY FOR WEB STARTUPS</h1>
    <p class="intro">Online website vulnerability scanning that tells you exactly<br>what needs fixing and how to to fix it.</p>

    <div class="feature" style="top:335px;">
      <span class="feature__tab">Accessible:</span>
      <p class="feature__text">VaultLarkly runs in the cloud and is accessible<br>from any computer, anywhere, any time.</p>
    </div>
    <div class="feature" style="top:424px;">
      <span class="feature__tab">Affordable:</span>
      <p class="feature__text">VaultLarkly uses a flexible pay-as-you-go<br>model that will fit any budget.</p>
    </div>
    <div class="feature feature--simple" style="top:520px;">
      <span class="feature__tab">Simple:</span>
      <p class="feature__text">Launch your scan using a simple 3-step<br>wizard and we'll do the rest.</p>
    </div>

    <footer class="footer">
      <p class="footer__url">www.vaultlarkly.example</p>
      <p class="footer__cta">TRY IT FREE TODAY!</p>
    </footer>
  </section>

  <section class="poster poster--right">
    <div class="poster__art" role="img" aria-label="Abstract angular backdrop in grey and green tones"></div>

    <div class="brand">
      <span class="brand__mark"></span>
      <span class="brand__name">VaultLarkly</span>
    </div>

    <h1 class="headline">SECURITY FOR WEB STARTUPS</h1>
    <p class="intro">Online website vulnerability scanning that tells you exactly<br>what needs fixing and how to to fix it.</p>

    <div class="feature" style="top:301px;">
      <span class="feature__tab">Accessible</span>
      <p class="feature__text">VaultLarkly runs in the cloud and is accessible<br>from any computer, anywhere, any time.</p>
    </div>
    <div class="feature" style="top:399px;">
      <span class="feature__tab">Affordable</span>
      <p class="feature__text">VaultLarkly uses a flexible pay-as-you-go<br>model that will fit any budget.</p>
    </div>
    <div class="feature" style="top:504px;">
      <span class="feature__tab">Simple</span>
      <p class="feature__text">Launch your scan using a simple 3-step<br>wizard and we'll do the rest.</p>
    </div>

    <footer class="footer">
      <p class="footer__url">www.vaultlarkly.example</p>
      <p class="footer__cta">TRY IT FREE TODAY!</p>
    </footer>
  </section>

</body>
</html>
```